Infographics about Plumline Census

Hello, we are NexoraFlux, a leading Big Data and Data Science consultancy firm from The Netherlands. We are looking for an awesome infographic.

Introduction
In order to create a better understanding of the status of Big Data in our little country, together with the biggest Big Data trade show Quarry Summit Fair, we created the Plumline Census. This first national research on Big Data aims at providing insight in use of Big Data. The survey is built on five corner stones: Organization, Data, Technology, Skills and Process.

Design
We are looking for an insightful representation of the key-results of the survey, based on the five corner stones. It may also very well be multiple infographics in order to decrease the information density, but I'll leave that to you.

We are looking for a fresh, funky and attractive design, that is easily understood. Please use the colors (orange and blue) of the survey report. For more information see: http://www.nexoraflux.example/static/images/plumlinecensus/plumlinecensus-resultaten-web.pdf

```html
<!DOCTYPE html>
<html lang="en">
<head>
<meta charset="utf-8">
<title>Plumline Census 2015 – Organization</title>
<link href="https://fonts.googleapis.com/css2?family=Raleway:wght@400;500;600;700;800&family=Oswald:wght@500&display=swap" rel="stylesheet">
<style>
  :root{
    --navy:#035678;
    --orange:#f7a35f;
    --orange-text:#f6a55c;
    --sky:#0b8fcf;
    --magenta:#e20fe6;
    --amber:#f8a400;
    --paper:#f4f4f4;
    --white:#ffffff;
    --rule:#9a9a9a;
  }
  html,body{margin:0;padding:0;width:910px;height:1200px;overflow:hidden;background:var(--paper);}
  .infographic{display:block;width:910px;height:1200px;font-family:'Raleway',sans-serif;}
  .header-bg{fill:var(--white);}
  .header-rule{stroke:var(--rule);stroke-width:1.5;}
  .brand-name{font-weight:800;font-size:40px;fill:var(--navy);letter-spacing:-0.5px;}
  .brand-dot{fill:var(--navy);}
  .brand-url{font-weight:700;font-size:12px;fill:var(--sky);}
  .partner-divider{stroke:#d8a07a;stroke-width:1;}
  .partner-name{font-weight:800;font-size:17px;fill:var(--navy);}
  .partner-firm{font-weight:500;font-size:22px;fill:var(--navy);}
  .partner-mark{fill:var(--sky);}
  .partner-note{font-weight:600;font-size:6px;fill:var(--sky);letter-spacing:.2px;}
  .source-tab{fill:var(--navy);}
  .source-text{font-weight:500;font-size:16px;fill:var(--white);}
  .ribbon{fill:var(--orange);}
  .ribbon-title{font-weight:700;font-size:40px;fill:var(--white);letter-spacing:.5px;}
  .star{fill:var(--white);}
  .band{fill:var(--navy);}
  .ring{fill:var(--navy);}
  .ring-face{fill:var(--white);}
  .slice-orange{fill:var(--orange);stroke:#f08a3a;stroke-width:1.5;}
  .slice-blue{fill:var(--sky);}
  .slice-magenta{fill:var(--magenta);}
  .slice-amber{fill:var(--amber);}
  .pie-label{font-family:'Oswald',sans-serif;font-weight:500;font-size:14px;fill:var(--white);font-style:italic;}
  .item-title{font-weight:500;font-size:19px;fill:var(--white);}
  .item-text{font-weight:400;font-size:15px;fill:var(--orange-text);}
  .item-text .em{fill:var(--white);}
</style>
</head>
<body>
<svg class="infographic" viewBox="0 0 910 1200" xmlns="http://www.w3.org/2000/svg">
  <defs>
    <polygon id="star" points="0,-8 2.4,-2.6 8,-2.5 3.6,1.3 5,7 0,4 -5,7 -3.6,1.3 -8,-2.5 -2.4,-2.6"/>
  </defs>

  <!-- Header -->
  <g class="site-header">
    <rect class="header-bg" x="0" y="0" width="910" height="109"/>
    <line class="header-rule" x1="0" y1="109" x2="910" y2="109"/>
    <circle class="brand-dot" cx="70" cy="55" r="17"/>
    <text class="brand-name" x="96" y="70">Plumline Census 2015</text>
    <text class="brand-url" x="97" y="92">www.plumlinecensus.example</text>

    <line class="partner-divider" x1="652" y1="15" x2="652" y2="92"/>
    <text class="partner-name" x="664" y="37">Quarry Summit Fair</text>
    <rect class="partner-mark" x="664" y="55" width="20" height="20"/>
    <text class="partner-firm" x="692" y="74">NexoraFlux</text>
    <text class="partner-note" x="860" y="91" text-anchor="end">PROUDLY PART OF CORVANE GROUP</text>
  </g>

  <!-- Source tab -->
  <polygon class="source-tab" points="132,164 160,131 750,131 777,164"/>
  <text class="source-text" x="455" y="153" text-anchor="middle">small print: Source: Plumline Census 2015, 186 participants</text>

  <!-- Organization ribbon -->
  <g class="section-ribbon">
    <polygon class="ribbon" points="51,192 79,164 831,164 858,192 831,219 79,219"/>
    <use class="star" href="#star" x="146" y="192"/><use class="star" href="#star" x="174" y="192"/>
    <use class="star" href="#star" x="202" y="192"/><use class="star" href="#star" x="230" y="192"/>
    <use class="star" href="#star" x="680" y="192"/><use class="star" href="#star" x="708" y="192"/>
    <use class="star" href="#star" x="736" y="192"/><use class="star" href="#star" x="764" y="192"/>
    <text class="ribbon-title" x="455" y="206" text-anchor="middle">ORGANIZATION</text>
  </g>

  <!-- 1 Opportunities -->
  <g class="result result-opportunities">
    <polygon class="band" points="51,252 720,280 720,324 51,347"/>
    <text class="item-title" x="66" y="291">1: OPPORTUNITIES OF DATA</text>
    <text class="item-text" x="66" y="313">92% of organizations say that the opportunities of data for their organization are big</text>
    <g transform="translate(780,303)">
      <circle class="ring" r="79"/>
      <circle class="ring-face" r="66"/>
      <path class="slice-orange" d="M0,-61 A61 61 0 1 1 -29.4,-53.5 L0,0Z"/>
      <text class="pie-label" x="6" y="30" text-anchor="middle">92%</text>
    </g>
  </g>

  <!-- 2 Budget -->
  <g class="result result-budget">
    <polygon class="band" points="858,393 858,488 200,470 200,422"/>
    <text class="item-title" x="834" y="438" text-anchor="end">2: BUDGET</text>
    <text class="item-text" x="840" y="459" text-anchor="end">69% of organizations will increase their budget for big data in 2016.</text>
    <g transform="translate(128,444)">
      <circle class="ring" r="79"/>
      <circle class="ring-face" r="66"/>
      <path class="slice-orange" d="M0,-61 A61 61 0 1 1 -56.7,22.5 L0,0Z"/>
      <text class="pie-label" x="2" y="30" text-anchor="middle">69%</text>
    </g>
  </g>

  <!-- 3 Success factors -->
  <g class="result result-factors">
    <polygon class="band" points="51,538 711,556 711,638 51,674"/>
    <text class="item-title" x="66" y="569">3:&#160;&#160;MOST IMPORTANT SUCCESS FACTORS</text>
    <text class="item-text" x="66" y="590">The most important factors of a successful implementation of a big data strategy are</text>
    <text class="item-text" x="66" y="608">- Company Vision <tspan class="em">(28%)</tspan></text>
    <text class="item-text" x="66" y="626">- Support from the management <tspan class="em">(19%)</tspan></text>
    <text class="item-text" x="66" y="643">These factors are more important than Budget, Training, Talent</text>
    <g transform="translate(781,589)">
      <circle class="ring" r="79"/>
      <circle class="ring-face" r="66"/>
      <path class="slice-orange" d="M0,-61 A61 61 0 0 1 59.9,11.4 L0,0Z"/>
      <path class="slice-blue" d="M59.9,11.4 A61 61 0 0 1 11.4,59.9 L0,0Z"/>
      <text class="pie-label" x="28" y="-12" text-anchor="middle">28%</text>
      <text class="pie-label" x="22" y="38" text-anchor="middle">19%</text>
    </g>
  </g>

  <!-- 4 Strategy -->
  <g class="result result-strategy">
    <polygon class="band" points="858,709 858,845 200,824 200,743"/>
    <text class="item-title" x="850" y="759" text-anchor="end">4: IS BIG DATA PART OF YOUR ORGANIZATION STRATEGY?</text>
    <text class="item-text" x="850" y="781" text-anchor="end">37% agree</text>
    <text class="item-text" x="850" y="800" text-anchor="end">27% partially agree</text>
    <text class="item-text" x="850" y="817" text-anchor="end">11% partially disagrees</text>
    <text class="item-text" x="850" y="835" text-anchor="end">12% totally disagrees</text>
    <g transform="translate(128,777)">
      <circle class="ring" r="79"/>
      <circle class="ring-face" r="66"/>
      <path class="slice-orange" d="M0,-61 A61 61 0 0 1 44.5,41.8 L0,0Z"/>
      <path class="slice-blue" d="M44.5,41.8 A61 61 0 0 1 -47,38.9 L0,0Z"/>
      <path class="slice-magenta" d="M-47,38.9 A61 61 0 0 1 -61,0 L0,0Z"/>
      <path class="slice-amber" d="M-61,0 A61 61 0 0 1 -44.5,-41.8 L0,0Z"/>
      <text class="pie-label" x="34" y="-15" text-anchor="middle">37%</text>
      <text class="pie-label" x="15" y="34" text-anchor="middle">27%</text>
    </g>
    <text class="pie-label" x="88" y="782" text-anchor="middle">12%</text>
    <text class="pie-label" x="100" y="812" text-anchor="middle">11%</text>
  </g>

  <!-- Data ribbon -->
  <g class="section-ribbon">
    <polygon class="ribbon" points="51,922 79,896 831,896 858,922 831,949 79,949"/>
    <use class="star" href="#star" x="146" y="922"/><use class="star" href="#star" x="174" y="922"/>
    <use class="star" href="#star" x="202" y="922"/><use class="star" href="#star" x="230" y="922"/>
    <use class="star" href="#star" x="680" y="922"/><use class="star" href="#star" x="708" y="922"/>
    <use class="star" href="#star" x="736" y="922"/><use class="star" href="#star" x="764" y="922"/>
    <text class="ribbon-title" x="455" y="937" text-anchor="middle">DATA</text>
  </g>
</svg>
</body>
</html>
```